Electrical company business card design.

Hi, were an electrical company in Brennock New Zealand called Quarneth Ltd. We focus mainly on high end residential and commercial so the card would be targeted towards that.
The card will be for myself, i am the director of the company.
Name: Derek Olstow
Position: Director/electrician
Phone: 021 387 9415
Email: derek@quarneth.co.nz
Location: Brennock
As for colors the the blue color in the logo is preferred, i also don't mind a black background option.
Target Market(s)
High end residential and commercial
Industry/Entity Type
Electrician
Contact Information for Business Card
Name: Derek Olstow Position: Director/Electrician Phone: 021 387 9415, Email: derek@quarneth.co.nz, Location: Brennock

```html
<!DOCTYPE html>
<html lang="en">
<head>
<meta charset="utf-8">
<title>Quarneth Ltd – Business Card</title>
<link rel="stylesheet" href="https://fonts.googleapis.com/css2?family=Roboto:wght@400;500&display=swap">
<style>
  :root {
    --bg: #c9cacc;
    --card: #ffffff;
    --blue-light: #40c3ee;
    --blue-deep: #2f6ccf;
    --blue-text: #2f82dc;
    --grey-dark: #8a8d91;
    --grey-light: #dfe2e6;
    --ink: #6f7276;
  }
  * { box-sizing: border-box; margin: 0; padding: 0; }
  html, body { width: 1200px; height: 900px; overflow: hidden; }
  body {
    background: var(--bg);
    font-family: "Roboto", Arial, sans-serif;
    position: relative;
  }
  .card {
    position: absolute;
    left: 250px;
    width: 700px;
    height: 400px;
    background: var(--card);
    box-shadow: 0 10px 30px rgba(0,0,0,0.18);
    overflow: hidden;
  }
  .card--front { top: 40px; }
  .card--back { top: 460px; }

  .edge-stripes { position: absolute; left: 0; bottom: 0; width: 700px; height: 70px; }

  .wordmark {
    font-weight: 500;
    color: var(--ink);
    letter-spacing: 2px;
    text-transform: uppercase;
    line-height: 1;
    white-space: nowrap;
  }
  .tagline {
    font-size: 13px;
    letter-spacing: 2.5px;
    color: var(--ink);
    text-transform: uppercase;
    margin-top: 10px;
    white-space: nowrap;
  }

  /* Front */
  .front-brand { position: absolute; left: 44px; top: 110px; }
  .front-brand .wordmark { font-size: 50px; }
  .brand-square {
    display: block;
    width: 30px; height: 30px;
    background: var(--blue-deep);
    margin-bottom: 22px;
  }
  .contact-block { position: absolute; left: 400px; top: 120px; width: 270px; }
  .person-name { font-size: 34px; font-weight: 500; color: var(--blue-text); white-space: nowrap; }
  .role-line { display: flex; align-items: center; gap: 12px; margin-top: 6px; }
  .person-role { font-size: 16px; color: var(--ink); letter-spacing: 0.5px; white-space: nowrap; }
  .role-rule { flex: 1; height: 1.5px; background: var(--blue-text); }
  .contact-list { list-style: none; margin-top: 22px; }
  .contact-item {
    display: flex; align-items: center; gap: 10px;
    font-size: 16px; color: var(--ink); margin-bottom: 14px;
  }
  .contact-item svg { width: 14px; height: 14px; flex: none; }
  .contact-item span { border-bottom: 1.5px solid var(--blue-text); padding-bottom: 2px; }

  /* Back */
  .back-brand {
    position: absolute; left: 0; right: 0; top: 132px;
    display: flex; flex-direction: column; align-items: center;
  }
  .back-brand .wordmark { font-size: 60px; display: flex; align-items: center; gap: 18px; }
  .back-brand .brand-square { margin: 0; width: 34px; height: 34px; }
</style>
</head>
<body>

<section class="card card--front" aria-label="Business card front">
  <div class="front-brand">
    <span class="brand-square"></span>
    <div class="wordmark">Quarneth</div>
    <div class="tagline">Wired for excellence</div>
  </div>

  <div class="contact-block">
    <div class="person-name">Derek Olstow</div>
    <div class="role-line">
      <span class="person-role">Director/Electrician</span>
      <span class="role-rule"></span>
    </div>
    <ul class="contact-list">
      <li class="contact-item">
        <svg viewBox="0 0 14 14" aria-hidden="true"><path d="M7 1a4 4 0 0 0-4 4c0 3 4 8 4 8s4-5 4-8a4 4 0 0 0-4-4zm0 5.5A1.5 1.5 0 1 1 7 3.5a1.5 1.5 0 0 1 0 3z" fill="#2f82dc"/></svg>
        <span>Brennock</span>
      </li>
      <li class="contact-item">
        <svg viewBox="0 0 14 14" aria-hidden="true"><path d="M3 1l2 3-1.2 1.4a8 8 0 0 0 4.8 4.8L10 9l3 2-1.2 2C6.5 13 1 7.5 1 2.2z" fill="#2f82dc"/></svg>
        <span>021 387 9415</span>
      </li>
    </ul>
  </div>

  <svg class="edge-stripes" viewBox="0 0 700 70" aria-hidden="true">
    <defs>
      <linearGradient id="band-front" x1="0" x2="1" y1="0" y2="0">
        <stop offset="0" stop-color="#40c3ee"/>
        <stop offset="1" stop-color="#2f6ccf"/>
      </linearGradient>
    </defs>
    <polygon points="0,20 385,20 372,70 0,70" fill="url(#band-front)"/>
    <polygon points="400,50 560,50 555,70 395,70" fill="#8a8d91"/>
    <polygon points="575,60 700,60 700,70 572,70" fill="#dfe2e6"/>
  </svg>
</section>

<section class="card card--back" aria-label="Business card back">
  <div class="back-brand">
    <div class="wordmark"><span class="brand-square"></span>Quarneth</div>
    <div class="tagline">Wired for excellence</div>
  </div>

  <svg class="edge-stripes" viewBox="0 0 700 70" aria-hidden="true">
    <defs>
      <linearGradient id="band-back" x1="0" x2="1" y1="0" y2="0">
        <stop offset="0" stop-color="#40c3ee"/>
        <stop offset="1" stop-color="#2f6ccf"/>
      </linearGradient>
    </defs>
    <polygon points="0,46 430,46 420,70 0,70" fill="url(#band-back)"/>
    <polygon points="445,54 600,54 594,70 438,70" fill="#8a8d91"/>
    <polygon points="615,62 700,62 700,70 612,70" fill="#dfe2e6"/>
  </svg>
</section>

</body>
</html>
```